UK vitamin company needs a packaging label design for new vitamin range

We have a logo, and we have the product. We now need some beautiful labels to go on the boxes which bring the product range to life.
We have 7 categories: Joint Care, Heart Heath, Brain Function, Immune System, Skin, Antioxidants and Probiotics. Each of these categories should have its own look within the plucky vitamin range. This can be quite subtle, but needs to be clearly visible and should be linked to the category e.g. 'Heart Health' might have a heart etc.
I have uploaded the logo, an example of the pack shape, and the sizing info for the label.
We are a fun brand, so please have some fun with this. We want the labels to be bold, and differentiated from the rest of the category.
Thanks
All images used must be 'rights free'. Many thanks
UK
It Company

```html
<!DOCTYPE html>
<html lang="en">
<head>
<meta charset="utf-8">
<title>Plucky Vitamins – Label Range</title>
<link href="https://fonts.googleapis.com/css2?family=Bebas+Neue&family=Oswald:wght@300;500;600&display=swap" rel="stylesheet">
<style>
  :root {
    --backdrop: #4b4f53;
    --label-white: #ffffff;
    --pattern-tone: #f6f6f6;
    --blue: #074ca4;
    --orange: #f27624;
    --green: #1fa23d;
  }
  html, body {
    margin: 0;
    padding: 0;
    width: 1200px;
    height: 1200px;
    overflow: hidden;
    background: var(--backdrop);
  }
  .canvas {
    position: relative;
    width: 1200px;
    height: 1200px;
  }
  .label {
    position: absolute;
    top: 130px;
    width: 540px;
    height: 913px;
    box-sizing: border-box;
    border-top: 6px solid var(--accent);
    background: var(--label-white);
    overflow: hidden;
  }
  .label--antioxidants { left: 43px; --accent: var(--blue); }
  .label--probiotics  { left: 619px; --accent: var(--orange); }

  .label__pattern {
    position: absolute;
    inset: 0;
    background: linear-gradient(160deg, var(--label-white) 0%, var(--pattern-tone) 50%, var(--label-white) 100%);
  }
  .label__band {
    position: absolute;
    left: 0;
    right: 0;
    bottom: 0;
    height: 29px;
    background: var(--accent);
  }

  .brand {
    position: absolute;
    top: 40px;
    left: 0;
    width: 100%;
    text-align: center;
    font-family: "Oswald", sans-serif;
    font-weight: 500;
    color: var(--orange);
  }
  .brand__name {
    position: relative;
    display: inline-block;
    font-size: 118px;
    line-height: 1;
    letter-spacing: 2px;
  }
  .brand__dot {
    position: absolute;
    top: 6px;
    right: -22px;
    width: 18px;
    height: 18px;
    border-radius: 50%;
    background: var(--green);
  }
  .brand__range {
    display: block;
    margin-top: 2px;
    font-size: 24px;
    letter-spacing: 9px;
    text-transform: uppercase;
  }

  .seal {
    position: absolute;
    left: 58px;
    top: 278px;
    width: 450px;
    height: 450px;
  }
  .seal__disc { fill: var(--accent); }
  .seal__ring { fill: none; stroke: var(--label-white); stroke-width: 2; }
  .seal__rule { stroke: var(--label-white); stroke-width: 2; }
  .seal text { fill: var(--label-white); text-anchor: middle; }
  .seal__arc-text {
    font-family: "Oswald", sans-serif;
    font-weight: 600;
    font-size: 18px;
    letter-spacing: 1px;
  }
  .seal__vitamins {
    font-family: "Oswald", sans-serif;
    font-weight: 300;
    font-size: 20px;
    letter-spacing: 1px;
  }
  .seal__title {
    font-family: "Bebas Neue", sans-serif;
    font-size: 74px;
    letter-spacing: 5px;
  }
  .seal__blurb {
    font-family: "Oswald", sans-serif;
    font-weight: 300;
    font-size: 13.5px;
  }
  .seal__count {
    font-family: "Bebas Neue", sans-serif;
    font-size: 40px;
  }
  .seal__unit {
    font-family: "Oswald", sans-serif;
    font-weight: 600;
    font-size: 19px;
  }
</style>
</head>
<body>
<main class="canvas">

  <article class="label label--antioxidants">
    <div class="label__pattern" role="img" aria-label="Faint light grey geometric line pattern across the label background"></div>

    <header class="brand">
      <span class="brand__name">plucky<span class="brand__dot"></span></span>
      <span class="brand__range">vitamins</span>
    </header>

    <svg class="seal" viewBox="0 0 450 450" aria-labelledby="seal-anti-title">
      <defs>
        <path id="arc-anti" d="M 65,225 A160,160 0 0 1 385,225"/>
      </defs>
      <circle class="seal__disc" cx="225" cy="225" r="225"/>
      <circle class="seal__ring" cx="225" cy="225" r="212"/>
      <text class="seal__arc-text"><textPath href="#arc-anti" startOffset="50%">• NATURAL ELEMENTS •</textPath></text>
      <text class="seal__vitamins" x="225" y="147">- B1 • B2 • B7 -</text>
      <line class="seal__rule" x1="67" y1="182" x2="384" y2="182"/>
      <text id="seal-anti-title" class="seal__title" x="227" y="252">ANTIOXIDANTS</text>
      <line class="seal__rule" x1="67" y1="271" x2="384" y2="271"/>
      <text class="seal__blurb" x="225" y="294">LOREM IPSUM DOLOR SIT AMET,</text>
      <text class="seal__blurb" x="225" y="311">CONSECTETUR ADIPISCING ELIT. CRAS</text>
      <text class="seal__blurb" x="225" y="328">ULLAMCORPER VELIT UT EGESTAS</text>
      <line class="seal__rule" x1="108" y1="342" x2="341" y2="342"/>
      <text x="225" y="411"><tspan class="seal__count">60</tspan> <tspan class="seal__unit">SOFTGELS</tspan></text>
    </svg>

    <div class="label__band"></div>
  </article>

  <article class="label label--probiotics">
    <div class="label__pattern" role="img" aria-label="Faint light grey geometric line pattern across the label background"></div>

    <header class="brand">
      <span class="brand__name">plucky<span class="brand__dot"></span></span>
      <span class="brand__range">vitamins</span>
    </header>

    <svg class="seal" viewBox="0 0 450 450" aria-labelledby="seal-pro-title">
      <defs>
        <path id="arc-pro" d="M 65,225 A160,160 0 0 1 385,225"/>
      </defs>
      <circle class="seal__disc" cx="225" cy="225" r="225"/>
      <circle class="seal__ring" cx="225" cy="225" r="212"/>
      <text class="seal__arc-text"><textPath href="#arc-pro" startOffset="50%">• NATURAL ELEMENTS •</textPath></text>
      <text class="seal__vitamins" x="225" y="147">- B1 • B2 • B7 -</text>
      <line class="seal__rule" x1="67" y1="182" x2="384" y2="182"/>
      <text id="seal-pro-title" class="seal__title" x="227" y="252">PROBIOTICS</text>
      <line class="seal__rule" x1="67" y1="271" x2="384" y2="271"/>
      <text class="seal__blurb" x="225" y="294">LOREM IPSUM DOLOR SIT AMET,</text>
      <text class="seal__blurb" x="225" y="311">CONSECTETUR ADIPISCING ELIT. CRAS</text>
      <text class="seal__blurb" x="225" y="328">ULLAMCORPER VELIT UT EGESTAS</text>
      <line class="seal__rule" x1="108" y1="342" x2="341" y2="342"/>
      <text x="225" y="411"><tspan class="seal__count">60</tspan> <tspan class="seal__unit">SOFTGELS</tspan></text>
    </svg>

    <div class="label__band"></div>
  </article>

</main>
</body>
</html>
```